Podcast cover art (not a logo)

I’m launching an audio-only podcast for parents of neurodivergent children. The podcast is meant to feel like a calm, trusted professional voice — not a brand or a performance.

Style direction:
--Clean and minimal
--Calm and grounded
--Professional, not playful
--Nothing flashy, loud, or busy
--No cartoon imagery

Content on the cover:
--Podcast title: Under the Quiet Surface
--Subtitle or tagline: Helping Neurodivergent Kids with Evidence, Not Blame (A Calmer Way to See Your Child)
--No episode numbers, no dates

Design preferences:
--Text-forward design
--Neutral or soft colors (muted blues, grays, off-whites)
--High contrast for readability at small sizes
--Simple, timeless font

What I do NOT want:
--A logo or branding system
--Illustrations of children or families
--Bright colors or playful graphics
--Trendy fonts or visual effects

Technical requirements:
--Square image
--3000 × 3000 pixels
--RGB color mode
--JPEG or PNG
--File size under 500 KB

Deliverables:
--Final cover art file
--Optional: one or two alternate background color versions

```html
<!DOCTYPE html>
<html lang="en">
<head>
<meta charset="utf-8">
<title>Under the Quiet Surface — Podcast Cover</title>
<link rel="stylesheet" href="https://fonts.googleapis.com/css2?family=Bebas+Neue&display=swap">
<style>
  :root {
    --band-light: #7aa7d6;
    --band-dark: #5384b4;
    --title-blue: #34689a;
    --title-soft: #7aa7d6;
    --tagline-gray: #666666;
    --tagline-dark: #2f2f2f;
    --paper-center: #ffffff;
    --paper-edge: #efefef;
  }
  html, body {
    margin: 0;
    padding: 0;
    width: 1200px;
    height: 1200px;
    overflow: hidden;
  }
  .cover {
    display: block;
    width: 1200px;
    height: 1200px;
    font-family: "Bebas Neue", "Oswald", sans-serif;
  }
  .band-light { fill: var(--band-light); }
  .band-dark { fill: var(--band-dark); }
  .title-strong { fill: var(--title-blue); }
  .title-soft { fill: var(--title-soft); }
  .tagline-main { fill: var(--tagline-gray); }
  .tagline-strong { fill: var(--tagline-dark); }
  .tagline-alt { fill: var(--tagline-gray); }
</style>
</head>
<body>
<svg class="cover" viewBox="0 0 1200 1200" xmlns="http://www.w3.org/2000/svg" role="img" aria-label="Under the Quiet Surface — Helping Neurodivergent Kids with Evidence, Not Blame">
  <defs>
    <radialGradient id="paper" cx="50%" cy="50%" r="70%">
      <stop offset="0%" stop-color="var(--paper-center)"/>
      <stop offset="55%" stop-color="#fbfbfb"/>
      <stop offset="100%" stop-color="var(--paper-edge)"/>
    </radialGradient>
  </defs>

  <rect class="background" width="1200" height="1200" fill="url(#paper)"/>

  <g class="bands-top">
    <rect class="band-light" x="0" y="0" width="1200" height="71"/>
    <rect class="band-dark" x="0" y="71" width="1200" height="70"/>
  </g>
  <g class="bands-bottom">
    <rect class="band-dark" x="0" y="1060" width="1200" height="69"/>
    <rect class="band-light" x="0" y="1129" width="1200" height="71"/>
  </g>

  <g class="title">
    <text class="title-strong" x="160" y="345" font-size="170"
          textLength="870" lengthAdjust="spacing">UNDER THE</text>
    <text class="title-soft" x="160" y="585" font-size="300"
          textLength="870" lengthAdjust="spacing">QUIET</text>
    <text class="title-strong" x="160" y="775" font-size="240"
          textLength="870" lengthAdjust="spacing">SURFACE</text>
  </g>

  <g class="tagline">
    <text class="tagline-main" x="160" y="849" font-size="81"
          textLength="870" lengthAdjust="spacingAndGlyphs">HELPING NEURODIVERGENT KIDS</text>
    <text class="tagline-strong" x="160" y="934" font-size="108"
          textLength="870" lengthAdjust="spacingAndGlyphs">WITH EVIDENCE, NOT BLAME</text>
    <text class="tagline-alt" x="160" y="990" font-size="71"
          textLength="870" lengthAdjust="spacingAndGlyphs">(A CALMER WAY TO SEE YOUR CHILD)</text>
  </g>
</svg>
</body>
</html>
```